Book cover for book entitled "Sweeping the Porch at Dawn ....and Keeping It Bright All Season Long"

I need a book cover for ebook and 6" x 9" paperback print book (brook press pod). I want a simple but "positive" cover with no gothic or darkness in design. I would prefer a "hopeful color scheme" in yellow, blue, green analogous colors and very easy to read main title "Sweeping the Porch at Dawn". I want the tag line of the title. "and keep it bright all season long" included on the cover please. I am not opposed to white in the color scheme I believe the graphic needs to somehow deal with doors, blocks, keys (perhaps a combination lock since the book is my story of healing from pancreatic cancer through faith, nutrition, and lifestyle changes). I am basically looking for the front cover from you but in a high definition format so it can be transferred to posters and banners for seminar displays. I am uploading my photo in case a designer would want to include a small copy of it in a design although I plan the photo to be on the back cover. The photo could, of course, be cropped.

I would also be interested in seeing a design with a woman  with arms folded and looking satisfied or victorious (happy) casually leaning against a closed door.    It can be very simple....

This graphic could be photo or drawing-even a good line drawing.   Almost whimsical would be okay.  This cover need not be highly complicated but I do want the title easy to read in small or large sizes for ebook and print book.

Reason: I have just changed to "committed" and some new "acceptances" have just come in.

Nutrition

Serif

fbee3e
acd037
33b7a4
34a6d8
3377b5

```html
<!DOCTYPE html>
<html lang="en">
<head>
<meta charset="utf-8">
<title>Sweeping the Porch at Dawn — Book Cover</title>
<link rel="stylesheet" href="https://fonts.googleapis.com/css2?family=Andada+Pro:wght@500;700;800&family=Oswald:wght@600&display=swap">
<style>
  :root {
    --sun-yellow: #fbee3e;
    --leaf-green: #acd037;
    --teal: #33b7a4;
    --sky-blue: #34a6d8;
    --deep-blue: #3377b5;
    --title-green: #3b6e38;
    --tagline-olive: #5d8a1c;
    --field-green: #6fa53a;
    --field-dark: #4d8a2c;
    --door-white: #ffffff;
    --door-shade: #e6eaec;
    --author-white: #ffffff;
  }
  * { margin: 0; padding: 0; box-sizing: border-box; }
  html, body { width: 802px; height: 1200px; overflow: hidden; background: #ffffff; }
  .cover {
    position: relative;
    width: 802px;
    height: 1200px;
    overflow: hidden;
  }
  .cover-scene {
    position: absolute;
    inset: 0;
    background:
      radial-gradient(ellipse 520px 260px at 60px 170px, rgba(251,238,62,0.9), rgba(251,238,62,0) 70%),
      radial-gradient(ellipse 600px 240px at 760px 90px, rgba(52,166,216,0.9), rgba(52,166,216,0) 70%),
      radial-gradient(ellipse 700px 200px at 420px 230px, rgba(172,208,55,0.55), rgba(172,208,55,0) 70%),
      linear-gradient(to bottom,
        #dfeecb 0%,
        #eef4f2 28%,
        #c9dcea 42%,
        #dfe9ef 56%,
        #eef2f1 63%,
        #d8e7a0 64%,
        #c9d84a 67%,
        var(--field-green) 72%,
        var(--field-dark) 100%);
  }
  .door {
    position: absolute;
    left: 247px;
    top: 412px;
    width: 293px;
    height: 674px;
    background: linear-gradient(to right, var(--door-shade) 0%, var(--door-white) 12%, var(--door-white) 88%, var(--door-shade) 100%);
    box-shadow: 0 0 60px 20px rgba(255,255,255,0.55), 0 6px 10px rgba(40,70,30,0.25);
  }
  .door::before {
    content: "";
    position: absolute;
    left: 24px;
    right: 24px;
    top: 24px;
    bottom: 0;
    border: 2px solid rgba(180,190,195,0.45);
    border-bottom: none;
  }
  .title-block {
    position: absolute;
    top: 56px;
    left: 0;
    width: 100%;
    text-align: center;
    color: var(--title-green);
    font-family: "Andada Pro", Georgia, serif;
  }
  .title-lead {
    display: block;
    font-size: 60px;
    font-weight: 700;
    line-height: 1;
  }
  .title-main {
    display: block;
    margin-top: 8px;
    font-size: 196px;
    font-weight: 800;
    line-height: 1;
    letter-spacing: 2px;
  }
  .tagline {
    position: absolute;
    top: 308px;
    left: 0;
    width: 100%;
    text-align: center;
    color: var(--tagline-olive);
    font-family: "Andada Pro", Georgia, serif;
    font-weight: 700;
    font-size: 40px;
    line-height: 1;
  }
  .author {
    position: absolute;
    bottom: 36px;
    left: 0;
    width: 100%;
    text-align: center;
    color: var(--author-white);
    font-family: "Oswald", "Arial Narrow", sans-serif;
    font-weight: 600;
    font-size: 46px;
    letter-spacing: 1px;
    text-shadow: 0 2px 4px rgba(0,0,0,0.45);
  }
</style>
</head>
<body>
  <main class="cover">
    <div class="cover-scene" role="img" aria-label="Photograph of a green meadow with yellow flowering fields under a bright blue-and-white cloudy sky"></div>
    <div class="door" role="img" aria-label="Photograph of a single closed white panelled door standing alone in the meadow, glowing with light"></div>

    <h1 class="title-block">
      <span class="title-lead">Sweeping the Porch at</span>
      <span class="title-main">DAWN</span>
    </h1>

    <p class="tagline">...and keep it bright all season long</p>

    <p class="author">MAREN HOLLOWAY</p>
  </main>
</body>
</html>
```